Tri-Fold Menu of Services for our Eyelash and Skin Care Spa

We need a beautiful spa service menu for our upscale spa in St. Charles Missouri. We specialize in providing treatments that are specific to the clients needs. Our services are eyelash extensions, skin care treatments, full body waxing and makeup application. Our spa colors are dark purples and greys and we are not opposed to additional colors that would complement those colors. We do a lot of eyelash extensions and while we do what those services listed we would like the skin care treatments to be in an area that would be noticed first. One of the attachments lists all of our services, descriptions and prices (please be sure to include all services and pricing. descriptions if possible). And our website has more information about us if needed. The website was not professionally done. So it DOESN'T represent our style exactly.

I HAVE ATTACHED A FEW PHOTOS BUT THEY DON'T HAVE TO BE USED.

Target Market(s)

women who would like to look their best, 35-55, annual income of 100,000+, she is usually busy and her children (if she has any) are high school age or older.

Industry/Entity Type

It Service

Font styles to use
Serif
Sans Serif

Requirements
Must have
• Must list all of our services. If it works to have the descriptions that would be great.
Nice to have
• If it works to have the descriptions of each service that would be great.

```html
<!DOCTYPE html>
<html lang="en">
<head>
<meta charset="utf-8">
<title>Facial &amp; Skin Treatments – Lumen Lash &amp; Skin Studio</title>
<link href="https://fonts.googleapis.com/css2?family=Lato:wght@700;900&family=Open+Sans:wght@400;600&display=swap" rel="stylesheet">
<style>
  :root {
    --ink: #242228;
    --ink-deep: #18171b;
    --plum: #6a3aa2;
    --plum-light: #8d5ccc;
    --plum-dark: #3e2266;
    --text: #ece9f0;
    --muted: #b9b3c3;
    --accent: #9b6ad8;
  }
  * { box-sizing: border-box; margin: 0; padding: 0; }
  html, body { width: 1200px; height: 767px; overflow: hidden; background: #e9e9e7; }
  .menu {
    position: relative; width: 1200px; height: 767px; overflow: hidden;
    background: linear-gradient(180deg, #2e2c33 0%, var(--ink) 55%, var(--ink-deep) 100%);
    font-family: "Open Sans", Arial, sans-serif; color: var(--text);
  }
  .art { position: absolute; inset: 0; }
  .fold { position: absolute; top: 0; bottom: 0; width: 1px; background: rgba(0,0,0,.35); }
  .block { position: absolute; }
  .title {
    font-family: "Lato", Arial, sans-serif; font-weight: 900; font-size: 31px;
    line-height: 1; letter-spacing: .5px; text-transform: uppercase; color: #fff;
  }
  .title .accent { color: var(--accent); }
  .service-name {
    font-family: "Lato", Arial, sans-serif; font-weight: 900; font-size: 15px;
    line-height: 1.1; color: #fff; margin-bottom: 4px;
  }
  .service-text { font-size: 10.8px; line-height: 1.42; color: var(--text); }
  .price {
    position: absolute; width: 62px; height: 62px; border-radius: 50%;
    background: radial-gradient(circle at 35% 30%, var(--plum-light), var(--plum) 55%, var(--plum-dark));
    box-shadow: 0 3px 8px rgba(0,0,0,.45);
    display: flex; flex-direction: column; align-items: center; justify-content: center;
    font-family: "Lato", Arial, sans-serif; color: #fff;
  }
  .price .amount { font-weight: 900; font-size: 19px; line-height: 1; }
  .price .amount sup { font-size: 9px; vertical-align: top; }
  .price .length { font-size: 7px; line-height: 1.2; opacity: .85; }
  .peels-title { font-family: "Lato", Arial, sans-serif; font-weight: 900; font-size: 26px; color: #fff; margin-bottom: 4px; }
  .peel { display: grid; grid-template-columns: 112px 46px 52px 1fr; align-items: baseline; font-size: 10px; line-height: 1.2; }
  .peel-name { font-family: "Lato", Arial, sans-serif; font-weight: 900; color: #fff; }
  .peel-single, .peel-time { color: var(--accent); }
  .peel-note { grid-column: 1 / -1; font-size: 9px; color: var(--muted); margin-bottom: 4px; }
  .studio-name {
    position: absolute; left: 836px; top: 690px;
    font-family: "Lato", Arial, sans-serif; font-weight: 900; font-size: 24px;
    letter-spacing: 3px; text-transform: uppercase; color: #f1eef4;
  }
</style>
</head>
<body>
<main class="menu">
  <svg class="art" width="1200" height="767" viewBox="0 0 1200 767">
    <defs>
      <linearGradient id="eyeTone" x1="0" y1="0" x2="1" y2="1">
        <stop offset="0" stop-color="#d7b8aa"/><stop offset=".6" stop-color="#b59486"/><stop offset="1" stop-color="#6f8590"/>
      </linearGradient>
      <linearGradient id="spaTone" x1="0" y1="0" x2="1" y2="1">
        <stop offset="0" stop-color="#e8c7b4"/><stop offset=".5" stop-color="#f2ddd0"/><stop offset="1" stop-color="#b8a39a"/>
      </linearGradient>
      <linearGradient id="frontTone" x1="0" y1="0" x2="0" y2="1">
        <stop offset="0" stop-color="#8e5a48"/><stop offset="1" stop-color="#6b3f33"/>
      </linearGradient>
    </defs>

    <g role="img" aria-label="Close-up photo of a client's eye with lash extensions">
      <path d="M0,500 C130,505 240,590 285,767 L0,767 Z" fill="url(#eyeTone)"/>
    </g>
    <g role="img" aria-label="Photo of a client receiving a skin treatment with a handheld device">
      <path d="M540,0 H800 V165 C690,165 600,195 548,262 C536,170 534,80 540,0 Z" fill="url(#spaTone)"/>
    </g>
    <g role="img" aria-label="Photo of the studio storefront on a brick wall">
      <path d="M800,767 V655 C900,615 1040,602 1200,600 V767 Z" fill="url(#frontTone)"/>
    </g>

    <g fill="none" stroke-linecap="round">
      <path d="M0,478 C150,482 270,580 315,767" stroke="#1b1a1e" stroke-width="18"/>
      <path d="M0,478 C150,482 270,580 315,767" stroke="var(--plum)" stroke-width="9"/>
      <path d="M0,458 C165,460 295,570 345,767" stroke="var(--plum-dark)" stroke-width="6"/>

      <path d="M800,180 C680,180 590,220 556,300 C520,390 478,570 448,767" stroke="#1b1a1e" stroke-width="18"/>
      <path d="M800,180 C680,180 590,220 556,300 C520,390 478,570 448,767" stroke="var(--plum)" stroke-width="9"/>
      <path d="M800,200 C695,200 612,238 578,312 C545,400 505,575 478,767" stroke="var(--plum-dark)" stroke-width="6"/>

      <path d="M800,640 C900,598 1040,585 1200,583" stroke="#1b1a1e" stroke-width="18"/>
      <path d="M800,640 C900,598 1040,585 1200,583" stroke="var(--plum)" stroke-width="9"/>
      <path d="M800,618 C900,578 1040,566 1200,565" stroke="var(--plum-dark)" stroke-width="6"/>
    </g>
  </svg>

  <div class="fold" style="left:400px"></div>
  <div class="fold" style="left:800px"></div>

  <!-- Panel one -->
  <h1 class="block title" style="left:36px; top:34px;">Facial <span class="accent">&amp; Skin</span><br>Treatments</h1>

  <section class="block" style="left:36px; top:118px; width:262px;">
    <h2 class="service-name">Essential Deep Cleansing Treatment</h2>
    <p class="service-text">This relaxing, purifying treatment consists of steaming, exfoliation, and an intense deeper cleansing of clogged pores. A skin type specific ampoule is gently massaged into the skin of your face, neck and décolleté, followed by a therapist selected mask. Beneficial for all skin types.</p>
  </section>
  <div class="price" style="left:312px; top:188px;"><span class="amount"><sup>$</sup>65</span><span class="length">60 minutes</span></div>

  <section class="block" style="left:36px; top:250px; width:262px;">
    <h2 class="service-name">Mini Facial</h2>
    <p class="service-text">This express facial is ideal for those on the go. Your skin is cleansed, lightly exfoliated and gently massaged. A pore refining mask is then applied, followed by a veil of light moisturizer.</p>
  </section>
  <div class="price" style="left:312px; top:300px;"><span class="amount"><sup>$</sup>48</span><span class="length">30 minutes</span></div>

  <section class="block" style="left:36px; top:362px; width:262px;">
    <h2 class="service-name">Aromatherapy Facial</h2>
    <p class="service-text">Our Aromatherapy facial will naturally enhance the facial benefits using fragrant oils extracted from flowers, fruits and herbs.</p>
  </section>
  <div class="price" style="left:312px; top:404px;"><span class="amount"><sup>$</sup>75</span><span class="length">60 minutes</span></div>

  <!-- Panel two -->
  <section class="block" style="left:576px; top:284px; width:214px;">
    <h2 class="service-name">Firmalux Lift &amp; Glow Treatment Facial</h2>
    <p class="service-text">Seeking a treatment with amazing instant results? Redefining radiance and facial contouring, this exclusively formulated treatment features the latest in freeze-dried technology to deliver instant results and cumulative skin care benefits. Ideal for any skin type showing signs of aging, or as the perfect instant repair boost when you want to look your best. Proven to perform, the Verdelle Firmalux Lift &amp; Glow facial renders your skin ultraluminous with a firmer, tighter and more youthful defined appearance.</p>
  </section>
  <div class="price" style="left:720px; top:552px;"><span class="amount"><sup>$</sup>95</span><span class="length">60 minutes</span></div>

  <section class="block" style="left:530px; top:620px; width:250px;">
    <h2 class="service-name">Soothing Botanique Treatment Facial</h2>
    <p class="service-text">This highly effective, soothing treatment calms redness and alleviates irritated or sensitive skin. A healing Propolis ampoule (natural ingredient collected by bees) is applied to desensitize the skin's surface and strengthen capillaries. A cooling liftoff mask is then applied to seal in the vitamin enriched beneficial ampoule.</p>
  </section>
  <div class="price" style="left:430px; top:690px; width:58px; height:58px;"><span class="amount"><sup>$</sup>100</span><span class="length">60 minutes</span></div>

  <!-- Panel three -->
  <div class="price" style="left:816px; top:30px;"><span class="amount"><sup>$</sup>150</span><span class="length">Package of 6</span></div>
  <section class="block" style="left:888px; top:32px; width:284px;">
    <h2 class="service-name">Radiance PhotoTherapy Treatment</h2>
    <p class="service-text">Uses heat and light energy to gently break up areas of excess pigment while stimulating the production of new collagen. Improved skin tone, less spots, fewer pink areas, less redness, reduction in fine lines and wrinkles. Diminishes pores and restores natural radiant glow of skin. Like laser treatments MicroPhotoTherapy treats skin with therapeutic light energy but unlike laser treatments, Micro PhotoTherapy features gentle waves of heat and light that improve the skin with no downtime and very little discomfort.</p>
  </section>

  <div class="price" style="left:816px; top:250px;"><span class="amount"><sup>$</sup>78</span><span class="length">60 minutes</span></div>
  <section class="block" style="left:888px; top:252px; width:284px;">
    <h2 class="service-name">Diamond Microdermabrasion Treatment</h2>
    <p class="service-text">With this treatment you will see softening of fine lines and wrinkles and smoothing of coarsely textured skin. Dull, stressed or congested skin will be brighter and clearer. The appearance of enlarged pores, and acne scars will be minimized. Your at home products will be able to penetrate deeper therefore, are more effective. Or add this to any facial or most peels for just $30.</p>
  </section>

  <section class="block" style="left:836px; top:412px; width:336px;">
    <h2 class="peels-title">Peels</h2>
    <div class="peel"><span class="peel-name">Acne Lift Peel</span><span class="peel-single">$50/1</span><span>$250/6</span><span class="peel-time">30 minutes</span><span class="peel-note">Mild to moderate Acne peel</span></div>
    <div class="peel"><span class="peel-name">Lightening Lift Peel</span><span class="peel-single">$50/1</span><span>$250/6</span><span class="peel-time">30 minutes</span><span class="peel-note">Pigmentation (sun/brown spots), uneven skin tone</span></div>
    <div class="peel"><span class="peel-name">Wrinkle Lift</span><span class="peel-single">$50/1</span><span>$250/6</span><span class="peel-time">30 minutes</span><span class="peel-note">Aging, fine lines and wrinkles</span></div>
    <div class="peel"><span class="peel-name">Signature Lift</span><span class="peel-single">$50/1</span><span>$250/6</span><span class="peel-time">30 minutes</span><span class="peel-note">Rosacea, dry/dehydrated</span></div>
    <div class="peel"><span class="peel-name">Perfection Lift</span><span class="peel-single">$100/1</span><span>$350/4</span><span class="peel-time">30 minutes</span></div>
  </section>

  <p class="studio-name">Lumen Lash &amp; Skin Studio</p>
</main>
</body>
</html>
```